Business Card Design Project

business cards to match the logo design reference 1970674
specific details to be provided asap - message to follow
hello - thank you for the logo design (reference 1970674) which we are very happy with. In terms of business cards you presented a couple of options ie blue front/white back and then the reverse. Can we start with the white front version but change the text details to black font?
Actual details are as follows;
Dorian Whitcombe
Managing Director
e dorianwhitcombe@velantra.com.au
t +61 2 7315 2946
m +61 422 517 639
Suite 307, Level 3, 82 Penhallow St
Sydney, NSW 2000, Australia
www.velantra.com.au

```html
<!DOCTYPE html>
<html lang="en">
<head>
<meta charset="utf-8">
<title>Velantra Business Card</title>
<link rel="stylesheet" href="https://fonts.googleapis.com/css2?family=Open+Sans:wght@400;600;700&display=swap">
<style>
  :root {
    --bg: #2b2b2b;
    --paper: #ffffff;
    --navy: #0b4a80;
    --navy-deep: #083a66;
    --sky: #2aa3dc;
    --sky-light: #45c4ee;
    --sky-pale: #c6e5f5;
    --ink: #1a1a1a;
    --rule: #1a8fd1;
  }
  * { margin: 0; padding: 0; box-sizing: border-box; }
  html, body { width: 1200px; height: 861px; overflow: hidden; }
  body {
    background: var(--bg);
    font-family: "Open Sans", Arial, sans-serif;
    position: relative;
  }
  .card {
    position: absolute;
    top: 276px;
    width: 540px;
    height: 309px;
    overflow: hidden;
  }
  .card--front { left: 40px; background: var(--paper); }
  .card--back { left: 620px; background: var(--navy); }

  /* front */
  .front-arcs { position: absolute; right: 0; top: 0; }
  .front-base { position: absolute; left: 0; bottom: 0; width: 100%; height: 7px; background: var(--rule); }
  .divider { position: absolute; left: 0; top: 150px; width: 100%; height: 1.5px; background: var(--rule); }
  .brand {
    position: absolute; left: 36px; top: 118px;
    display: flex; align-items: center; gap: 10px;
  }
  .brand-dot { width: 18px; height: 18px; border-radius: 50%; background: var(--sky); }
  .brand-name { font-size: 24px; font-weight: 600; color: #4a4a4a; letter-spacing: 0.5px; }
  .person { position: absolute; right: 34px; top: 112px; text-align: right; }
  .person-name {
    font-size: 22px; font-weight: 400; color: var(--rule);
    font-variant: small-caps; letter-spacing: 0.5px; line-height: 1;
  }
  .person-role {
    margin-top: 14px; font-size: 10.5px; font-weight: 700; color: var(--ink);
    letter-spacing: 0.6px;
  }
  .contact-list { position: absolute; list-style: none; font-size: 11.5px; color: var(--ink); }
  .contact-list li { display: flex; align-items: center; gap: 9px; height: 19px; }
  .contact-list svg { width: 11px; height: 11px; fill: var(--rule); flex: none; }
  .contact-list--phones { left: 36px; top: 226px; }
  .contact-list--place { right: 34px; top: 176px; width: 240px; }
  .contact-list--place .line2 { padding-left: 20px; }

  /* back */
  .back-arcs { position: absolute; right: 0; top: 0; }
  .back-brand {
    position: absolute; left: 42px; top: 182px;
    font-size: 58px; font-weight: 700; color: var(--sky-light);
    letter-spacing: 1px; line-height: 1;
  }
  .back-web {
    position: absolute; left: 46px; top: 254px;
    font-size: 15px; font-weight: 400; color: #ffffff; letter-spacing: 5px;
  }
</style>
</head>
<body>

<section class="card card--front" aria-label="Card front">
  <svg class="front-arcs" width="200" height="200" viewBox="0 0 200 200" aria-hidden="true">
    <path d="M120 0 A150 150 0 0 1 200 60 L200 100 A170 170 0 0 0 95 0 Z" fill="var(--sky-pale)"/>
    <path d="M165 0 A110 110 0 0 1 200 25 L200 45 A125 125 0 0 0 148 0 Z" fill="var(--sky-pale)"/>
  </svg>
  <div class="brand">
    <span class="brand-dot"></span>
    <span class="brand-name">Velantra</span>
  </div>
  <div class="divider"></div>
  <div class="person">
    <div class="person-name">Dorian Whitcombe</div>
    <div class="person-role">MANAGING DIRECTOR</div>
  </div>

  <ul class="contact-list contact-list--place">
    <li><svg viewBox="0 0 12 12"><circle cx="6" cy="6" r="5.5"/></svg>www.velantra.com.au</li>
    <li><svg viewBox="0 0 12 12"><path d="M6 0a4 4 0 0 1 4 4c0 3-4 8-4 8S2 7 2 4a4 4 0 0 1 4-4z"/></svg>Suite 307, Level 3, 82 Penhallow St</li>
    <li class="line2">Sydney, NSW 2000, Australia</li>
  </ul>

  <ul class="contact-list contact-list--phones">
    <li><svg viewBox="0 0 12 12"><path d="M2 0h3l1 3-2 1.5a7 7 0 0 0 3.5 3.5L9 6l3 1v3a2 2 0 0 1-2 2A10 10 0 0 1 0 2a2 2 0 0 1 2-2z"/></svg>+61 2 7315 2946</li>
    <li><svg viewBox="0 0 12 12"><rect x="3" y="0" width="6" height="12" rx="1"/></svg>+61 422 517 639</li>
    <li><svg viewBox="0 0 12 12"><path d="M0 2h12v8H0z M0 2l6 5 6-5"/></svg>dorianwhitcombe@velantra.com.au</li>
  </ul>
  <div class="front-base"></div>
</section>

<section class="card card--back" aria-label="Card back">
  <svg class="back-arcs" width="300" height="309" viewBox="0 0 300 309" aria-hidden="true">
    <path d="M0 0 H300 V309 H60 A300 300 0 0 0 0 0 Z" fill="var(--navy-deep)"/>
    <path d="M70 0 H110 A320 320 0 0 1 230 309 H150 A330 330 0 0 0 70 0 Z" fill="var(--sky)"/>
    <path d="M150 0 H180 A300 300 0 0 1 275 309 H250 A310 310 0 0 0 150 0 Z" fill="var(--sky)"/>
    <path d="M215 0 H235 A280 280 0 0 1 300 240 V300 A290 290 0 0 0 215 0 Z" fill="var(--sky)"/>
  </svg>
  <div class="back-brand">VELANTRA</div>
  <div class="back-web">WWW.VELANTRA.COM.AU</div>
</section>

</body>
</html>
```